Small dedicated blog website

I have recently had a logo designed for my growing personal hobby, I document my adventures around the world in video form (www.vidloop.example/harwickroams.com) I am now trying to create a small blog website with easy access to my other social networks to start to create a home base for all the videos and content I create, I would like a simple website with a focus on blog posts and access to my other social networks, pictagram (harwickroams), friendsheet (harwickroams), quicksnip (dalemarwick)

My current website can be viewed at www.harwickroams.example

Please contact me for any further information to help this project

Many thanks!

I do not expect a fully coded website, simply designs and graphics

Industry/Entity Type

Social

Font styles to use
Sans Serif

Requirements
Must have
• area for scrollr blog placement, access to social media links

```html
<!DOCTYPE html>
<html lang="en">
<head>
<meta charset="utf-8">
<title>Harwick Roams – Blog Layout</title>
<link rel="stylesheet" href="https://fonts.googleapis.com/css2?family=Montserrat:wght@300;400;700&family=Arimo:wght@400&display=swap">
<style>
:root{
  --dark:#2a2c2f;
  --dark-2:#1f2023;
  --grey:#b1b1b1;
  --grey-light:#bdbdbd;
  --paper:#ffffff;
  --white:#ffffff;
  --note-bg:#000000;
  --note-red:#ff3b30;
  --mark-red:#e8383b;
  --track:#e6e6e6;
}
*{margin:0;padding:0;box-sizing:border-box}
html,body{width:1200px;height:1000px;overflow:hidden;background:var(--grey)}
.page{position:relative;width:1200px;height:1000px;overflow:hidden;background:var(--grey);font-family:"Montserrat",sans-serif}
.side{position:absolute;left:0;top:0;width:273px;height:1000px;background:linear-gradient(180deg,var(--dark) 0%,#3a3c40 55%,#55575b 100%)}
.side-photo{position:absolute;left:0;top:520px;width:273px;height:480px;background:linear-gradient(180deg,rgba(70,72,76,0) 0%,#6b6d71 60%,#7c7e82 100%)}
.header{position:absolute;left:0;top:60px;width:1200px;height:232px;background:linear-gradient(180deg,var(--dark-2),var(--dark))}
.brand{position:absolute;right:55px;top:140px;color:var(--white);font-weight:700;font-size:16px;letter-spacing:.5px}
.nav-rule{position:absolute;left:273px;top:235px;width:872px;height:2px;background:var(--white)}
.nav{position:absolute;top:244px;left:0;width:1200px;color:var(--white);font-size:38px;font-weight:400;line-height:44px}
.nav a{position:absolute;color:inherit;text-decoration:none}
.nav .is-active{font-weight:700}
.content-bg{position:absolute;left:1068px;top:292px;width:132px;height:708px;background:var(--grey-light)}
.add-btn{position:absolute;left:855px;top:362px;width:32px;height:20px;background:#8f8f8f;border-radius:3px;color:#fff;font-size:18px;font-weight:700;text-align:center;line-height:20px}
.post{position:absolute;left:355px;top:410px;width:713px;height:590px;background:var(--paper)}
.post-photo{position:absolute;left:75px;width:560px}
.post-photo.one{top:57px;height:275px;background:linear-gradient(135deg,#3b3838,#d9d6cf 45%,#e8e6e0 70%,#3a3838)}
.post-photo.two{top:345px;height:245px;background:linear-gradient(180deg,#cbc6bd,#e2ded7)}
.scroll{position:absolute;left:1130px;top:510px}
.social{position:absolute;left:177px;width:52px;height:52px}
.social span{position:absolute;inset:0;display:flex;align-items:center;justify-content:center;color:var(--white);font-size:7px;font-weight:700}
.contact{position:absolute;left:23px;top:822px;width:228px;text-align:center;color:var(--white);text-decoration:none}
.contact .name{display:block;font-size:19px;font-weight:300;letter-spacing:.3px}
.contact .mail{display:block;font-size:10px;font-weight:400;margin-top:1px}
.mark{position:absolute;border:3px solid var(--mark-red)}
.mark.circle{border-radius:50%}
.note{position:absolute;background:var(--note-bg);color:var(--note-red);font-family:"Arimo",sans-serif;font-size:18px;line-height:26px}
</style>
</head>
<body>
<div class="page">
  <div class="side"></div>
  <div class="side-photo" role="img" aria-label="Sliding background photo of a traveller silhouette"></div>

  <header class="header"></header>
  <div class="brand">HARWICKROAMS.COM</div>
  <div class="nav-rule"></div>
  <nav class="nav">
    <a class="is-active" style="left:300px" href="#">BLOG</a>
    <a style="left:466px" href="#">VIDEO</a>
    <a style="left:636px" href="#">PHOTO</a>
    <a style="left:1081px" href="#">BIO</a>
  </nav>

  <div class="content-bg"></div>
  <div class="add-btn">+</div>
  <article class="post">
    <div class="post-photo one" role="img" aria-label="Blog post photo of a travel card"></div>
    <div class="post-photo two" role="img" aria-label="Blog post photo of a residence document"></div>
  </article>
  <svg class="scroll" width="26" height="490" viewBox="0 0 26 490">
    <line x1="13" y1="0" x2="13" y2="490" stroke="var(--track)" stroke-width="2"/>
    <circle cx="13" cy="62" r="11" fill="#f2f2f2" stroke="#9a9a9a" stroke-width="1"/>
  </svg>

  <a class="social" style="top:384px" href="#"><svg width="52" height="52"><circle cx="26" cy="26" r="24" fill="none" stroke="#fff" stroke-width="3"/></svg><span>friendsheet</span></a>
  <a class="social" style="top:470px" href="#"><svg width="52" height="52"><circle cx="26" cy="26" r="24" fill="none" stroke="#fff" stroke-width="3"/></svg><span>vidloop</span></a>

  <a class="contact" href="mailto:dale@harwickroams.example">
    <span class="name">DALE MARWICK</span>
    <span class="mail">DALE@HARWICKROAMS.EXAMPLE</span>
  </a>

  <div class="mark" style="left:267px;top:208px;width:168px;height:116px"></div>
  <div class="mark" style="left:1027px;top:209px;width:168px;height:116px"></div>
  <div class="mark" style="left:23px;top:805px;width:229px;height:79px"></div>
  <div class="mark circle" style="left:13px;top:540px;width:134px;height:134px"></div>

  <div class="note" style="left:268px;top:338px;width:306px;height:141px;padding:21px 27px">When you slelect menu,<br>get change into bold style.<br><br>‘Avian’ font.</div>
  <div class="note" style="left:885px;top:342px;width:304px;height:158px;padding:36px 21px;font-size:19px">Bio menu should be pop-up window. And allow to open above any other pages.</div>
  <div class="note" style="left:160px;top:495px;width:620px;height:221px;padding:20px 18px;font-size:20px;line-height:30px">If you can, slide background images would be nice. It will be more interest.<br>If you do, To make it right size and position, use pixelforge’s smart object function.<br>Goto ‘frame’ group, double click on thumnail of ‘b.image’. New window with guide line will open.</div>
  <div class="note" style="left:265px;top:805px;width:629px;height:106px;padding:27px 17px;font-size:19px">Make sure floating contact info. at this position on the screen. and hyperlinked.</div>
</div>
</body>
</html>
```